I need a business card for a new small local scaffolding company. I supply and erect all types of scaffolding for any access need. I thought I could put a safety hat on the Q in NQ to emphasize the 'safe' in KORVELTA. Just a thought.

Industry/Entity Type

Safety

Contact Information for Business Card

KORVELTA NQ , Rob Tenwick , All scaffold & access solutions , Hire , Sales , Transport ,email korveltanq@brisomail.net , 0438710536, fully accredited , abn 47290318854

```html
<!DOCTYPE html>
<html lang="en">
<head>
<meta charset="utf-8">
<title>Korvelta NQ business card</title>
<link href="https://fonts.googleapis.com/css2?family=Quicksand:wght@400;500;600;700&display=swap" rel="stylesheet">
<style>
  :root {
    --brand-blue: #1cb0e8;
    --card-white: #ffffff;
    --card-shade: #f1f2f3;
    --ink-dark: #2c2f33;
    --ink-muted: #5a6068;
    --backdrop: #e8e3d9;
  }
  * { box-sizing: border-box; margin: 0; padding: 0; }
  html, body {
    width: 1071px; height: 1200px; overflow: hidden;
    background: var(--backdrop);
    font-family: "Quicksand", sans-serif;
  }
  .canvas {
    position: relative; width: 1071px; height: 1200px;
    display: flex; flex-direction: column; align-items: center; justify-content: center; gap: 90px;
  }
  .card {
    position: relative; width: 780px; height: 446px;
    background: linear-gradient(135deg, var(--card-white) 0%, var(--card-shade) 100%);
    box-shadow: 0 14px 30px rgba(0,0,0,0.18);
    overflow: hidden;
  }
  /* front */
  .card-front .side-band {
    position: absolute; top: 0; right: 0; width: 150px; height: 100%;
    background: var(--brand-blue);
  }
  .card-front .services {
    position: absolute; right: 34px; bottom: 36px;
    color: var(--card-white); font-size: 17px; font-weight: 500; line-height: 1.6;
    writing-mode: vertical-rl; transform: rotate(180deg);
    white-space: nowrap;
  }
  .card-front .brand-name {
    position: absolute; top: 78px; left: 250px;
    color: var(--brand-blue); font-size: 46px; font-weight: 500; letter-spacing: 2px;
    white-space: nowrap;
  }
  .person {
    position: absolute; left: 0; top: 224px; display: flex; align-items: flex-start; gap: 22px;
  }
  .person-marker { width: 30px; height: 48px; background: var(--brand-blue); }
  .person-name { color: var(--brand-blue); font-size: 21px; font-weight: 600; letter-spacing: 1px; }
  .person-role { color: var(--ink-dark); font-size: 18px; font-weight: 600; letter-spacing: 1px; margin-top: 2px; }
  .contact-list {
    position: absolute; left: 52px; top: 302px; list-style: none;
    display: flex; flex-direction: column; gap: 7px;
    color: var(--ink-muted); font-size: 15px; font-weight: 500;
  }
  .contact-list li { display: flex; align-items: center; gap: 12px; white-space: nowrap; }
  .contact-list svg { width: 14px; height: 14px; flex: none; }
  /* back */
  .card-back .brand-name {
    position: absolute; inset: 0; display: flex; align-items: center; justify-content: center;
    color: var(--brand-blue); font-size: 60px; font-weight: 500; letter-spacing: 3px;
  }
  .card-back .base-edge {
    position: absolute; left: 0; bottom: 0; width: 100%; height: 14px; background: var(--brand-blue);
  }
</style>
</head>
<body>
<main class="canvas">
  <section class="card card-front" aria-label="Card front">
    <div class="side-band"></div>
    <p class="services">All scaffold &amp; access solutions<br>Hire · Sales · Transport</p>
    <h1 class="brand-name">KORVELTA NQ</h1>
    <div class="person">
      <span class="person-marker"></span>
      <div>
        <p class="person-name">ROB TENWICK</p>
        <p class="person-role">GENERAL MANAGER</p>
      </div>
    </div>
    <ul class="contact-list">
      <li><svg viewBox="0 0 14 14"><path d="M3 1 L5 1 L6 4 L4.5 5.3 Q6 8.5 8.7 9.5 L10 8 L13 9 L13 11 Q12.5 13 10.5 13 Q2 11.5 1 3.5 Q1 1 3 1 Z" fill="var(--brand-blue)"/></svg>0438 710 536</li>
      <li><svg viewBox="0 0 14 14"><rect x="1" y="3" width="12" height="8" fill="var(--brand-blue)"/><path d="M1 3 L7 8 L13 3" fill="none" stroke="#fff" stroke-width="1.2"/></svg>korveltanq@brisomail.net</li>
      <li><svg viewBox="0 0 14 14"><rect x="2" y="2" width="10" height="10" fill="none" stroke="var(--brand-blue)" stroke-width="1.8"/></svg>ABN 47 290 318 854</li>
      <li><svg viewBox="0 0 14 14"><path d="M2 7.5 L5.5 11 L12 3.5" fill="none" stroke="var(--brand-blue)" stroke-width="2"/></svg>Fully accredited</li>
      <li><svg viewBox="0 0 14 14"><circle cx="7" cy="7" r="6" fill="var(--brand-blue)"/></svg>Supply &amp; erect all scaffold types</li>
    </ul>
  </section>

  <section class="card card-back" aria-label="Card back">
    <h2 class="brand-name">KORVELTA NQ</h2>
    <div class="base-edge"></div>
  </section>
</main>
</body>
</html>
```